Business Card Design and Stationary design for consulting firm

Harbourline Sourcing are looking for a new business card design and a design for their A4 letterhead / A4 invoices.

We are seeking to heavily increase our brand awareness and require a business card that's professional in appearance but also shows flare and innovation. A card design that people will remember.

About Us
Harbourline Sourcing are `The Sourcing Crew’.
Our mission is to be one of Australia’s greatest companies. Our aim is to help our customers achieve the best result from their purchasing experience.

Our Requirement:
• IMPACT! IMPACT! IMPACT!
• BUSINESS & PROFESSIONAL LOOKING

• Our business colours are orange, blue and green (See the logo attached).

We have provided an Art Design specification (attached) that needs to be followed for you to win the design. This also has the font, which is used on the logo.

We are after a two sided business card

Side One should have the:
The company Logo
The Sourcing Crew
www.harbourlinesourcing.com.au
Procure | Personnel | Probity & Privacy
Sydney | Melbourne | Adelaide | Brisbane

Side Two
Logo (optional)
Harbourline Sourcing (optional)
Employee details (details listed below)

The above format is our preferred option, but if you think you can come up with something better, feel free to put it forward.

We are leaving the design up to you, but it must incorporate the logo.

We will need a template that we can change the employee details on, as we will be adding more staff over the coming months.

The details below are for one employee per card with the same design.
------------------------

Employee Details:

Marcus Del Arroyo MBA, MMgmtStratProc
Principal Consultant
0491 372 618
Marcus@harbourlinesourcing.com.au

Brianna Tolley
Consulting Manager
0462 915 308
Brianna@harbourlinesourcing.com.au

Our website is www.harbourlinesourcing.com.au

The Letterhead / invoice needs to incorporate:
the company Logo
The Sourcing Crew
Sydney | Melbourne | Adelaide | Brisbane but otherwise the design is over to you.

This file needs to be delivered in word format as other detail will be added to the documents.

We look forward to you award winning designs. If you require any further information please feel free to contact us.

Regards
Harbourline Sourcing

Target Market(s)

Our Target market is companies with 80+ employees. The market we segment is heavily male based, between the ages of 35-55 years of age.

Industry/Entity Type

Consulting

Contact Information for Business Card

See Project Description

Font styles to use
Other font styles liked:
• See Art Specification

Requirements
Must have
• Company Colours, See Project Description
Should not have
• Be outside the Art specification guidelines

```html
<!DOCTYPE html>
<html lang="en">
<head>
<meta charset="utf-8">
<title>Harbourline Sourcing – Business Card</title>
<link href="https://fonts.googleapis.com/css2?family=Open+Sans:wght@400;600;700&display=swap" rel="stylesheet">
<style>
  :root {
    --page-bg: #2a2a2a;
    --card-dark: #434345;
    --card-band: #555658;
    --card-light: #ffffff;
    --text-dark: #333335;
    --text-muted: #8a8a8c;
    --text-faint: #9c9c9e;
    --brand-blue: #1f7bc4;
    --brand-green: #6cbf2a;
    --brand-orange: #f26b1d;
  }
  * { margin: 0; padding: 0; box-sizing: border-box; }
  html, body {
    width: 1200px; height: 1200px; overflow: hidden;
    background: var(--page-bg);
    font-family: "Open Sans", Arial, sans-serif;
  }
  .card {
    position: absolute; left: 220px;
    width: 760px; height: 465px;
    background: var(--card-dark);
    overflow: hidden;
    box-shadow: 0 10px 30px rgba(0,0,0,.45);
  }
  .card--front { top: 105px; }
  .card--back { top: 630px; }
  .card__art { position: absolute; inset: 0; }
  .layer { position: absolute; left: 0; width: 100%; text-align: center; }

  /* front */
  .front-brand {
    top: 150px; font-size: 50px; font-weight: 700;
    color: var(--text-muted); letter-spacing: 2px;
    display: flex; justify-content: center; align-items: center; gap: 16px;
  }
  .brand-dot { width: 22px; height: 22px; border-radius: 50%; background: var(--brand-orange); flex: none; }
  .front-tagline {
    top: 228px; font-size: 20px; color: var(--text-muted);
    letter-spacing: 5px; text-transform: uppercase;
  }
  .front-services {
    top: 388px; font-size: 19px; color: var(--text-faint);
    letter-spacing: 1px; text-transform: uppercase;
  }

  /* back */
  .back-brand {
    top: 150px; font-size: 32px; font-weight: 700;
    color: var(--text-dark); letter-spacing: 2px;
    display: flex; justify-content: center; align-items: center; gap: 12px;
  }
  .back-brand .brand-dot { width: 15px; height: 15px; }
  .staff { top: 205px; color: var(--text-dark); font-size: 16px; line-height: 1.55; }
  .staff__name { font-size: 20px; }
  .staff__name strong { color: var(--brand-blue); font-weight: 700; text-transform: uppercase; }
  .staff__role { font-size: 14px; text-transform: uppercase; margin-bottom: 6px; }
  .staff__label { font-weight: 600; }
  .back-cities {
    top: 418px; font-size: 17px; color: #ffffff;
    letter-spacing: 2px; text-transform: uppercase;
  }
</style>
</head>
<body>

<section class="card card--front">
  <svg class="card__art" viewBox="0 0 760 465" aria-hidden="true">
    <path d="M0,345 Q380,265 760,305 L760,465 L0,465 Z" fill="var(--card-band)"/>
    <path d="M0,345 Q380,265 760,305" fill="none" stroke="#6a6b6d" stroke-width="2"/>
  </svg>
  <div class="layer front-brand"><span class="brand-dot"></span><span>Harbourline Sourcing</span></div>
  <div class="layer front-tagline">The Sourcing Crew</div>
  <div class="layer front-services">Procurement | Personnel | Probity &amp; Privacy</div>
</section>

<section class="card card--back">
  <svg class="card__art" viewBox="0 0 760 465" aria-hidden="true">
    <defs>
      <linearGradient id="swoosh" x1="0" y1="0" x2="1" y2="0">
        <stop offset="0" stop-color="var(--brand-green)"/>
        <stop offset="0.3" stop-color="var(--brand-green)" stop-opacity="0"/>
        <stop offset="0.6" stop-color="var(--brand-orange)" stop-opacity="0"/>
        <stop offset="1" stop-color="var(--brand-orange)"/>
      </linearGradient>
    </defs>
    <path d="M0,190 C200,20 620,20 760,300 L760,400 L0,400 Z" fill="var(--card-light)"/>
    <path d="M0,190 C200,20 620,20 760,300" fill="none" stroke="url(#swoosh)" stroke-width="9"/>
    <rect x="0" y="400" width="760" height="65" fill="var(--card-dark)"/>
  </svg>
  <div class="layer back-brand"><span class="brand-dot"></span><span>Harbourline Sourcing</span></div>
  <div class="layer staff">
    <div class="staff__name"><strong>Marcus Del Arroyo</strong> MBA, MMgmt StratProc</div>
    <div class="staff__role">Principal Consultant</div>
    <div><span class="staff__label">[P]</span> 0491 372 618</div>
    <div><span class="staff__label">[E]</span> Marcus@harbourlinesourcing.com.au</div>
    <div><span class="staff__label">[W]</span> www.harbourlinesourcing.com.au</div>
  </div>
  <div class="layer back-cities">Sydney | Melbourne | Adelaide | Brisbane</div>
</section>

</body>
</html>
```